Brightwave Business Card

Professional Business Card Design required using the attached contact information.

Contact information can be rearranged as required.

The company is a new start up venture developing solar systems, the branding should be in keeping with that of one of the investors whose website is as follows https://www.quorvex.com/

```html
<!DOCTYPE html>
<html lang="en">
<head>
<meta charset="utf-8">
<title>Brightwave Renewables Business Card</title>
<link rel="stylesheet" href="https://fonts.googleapis.com/css2?family=Roboto:wght@300;400&display=swap">
<style>
  :root {
    --brand-green: #2a6756;
    --ink: #1d1d1d;
    --muted: #555555;
    --icon-grey: #b9b9b9;
    --paper: #ffffff;
    --page: #f3f3f3;
  }
  * { box-sizing: border-box; margin: 0; padding: 0; }
  html, body {
    width: 1200px; height: 1200px; overflow: hidden;
    background: var(--page);
    font-family: "Roboto", Arial, sans-serif;
  }
  .card {
    position: absolute; left: 220px;
    width: 760px; height: 434px;
    background: var(--paper);
    border-radius: 28px;
    overflow: hidden;
    box-shadow: 0 6px 18px rgba(0,0,0,0.18);
  }
  .card--front { top: 110px; }
  .card--back { top: 650px; }

  .footer-band {
    position: absolute; left: 0; right: 0; bottom: 0;
    height: 34px; background: var(--brand-green);
  }
  .footer-tab {
    position: absolute; bottom: 0;
    width: 330px; height: 62px;
    background: var(--brand-green);
    border-radius: 26px 26px 0 0;
    color: var(--paper);
    font-size: 14px; font-weight: 400;
    text-align: center; line-height: 34px;
    white-space: nowrap;
  }
  .card--front .footer-tab { left: 315px; }
  .card--back .footer-tab { left: 215px; }

  .company-name {
    position: absolute;
    color: var(--ink);
    font-size: 40px;
    font-weight: 400;
    white-space: nowrap;
    line-height: 1;
  }
  .card--front .company-name { top: 92px; left: 40px; }
  .card--back .company-name { top: 197px; left: 0; right: 0; text-align: center; }

  .identity {
    position: absolute; top: 188px; left: 30px; width: 340px;
    text-align: right;
  }
  .identity__name { font-size: 36px; font-weight: 400; color: var(--ink); line-height: 1.1; }
  .identity__role { font-size: 22px; font-weight: 300; color: var(--brand-green); margin-top: 2px; }
  .identity__company, .identity__address { font-size: 15px; color: var(--muted); line-height: 1.35; }
  .identity__company { margin-top: 6px; }

  .divider {
    position: absolute; left: 388px; top: 180px;
    width: 2px; height: 120px; background: var(--brand-green);
  }

  .contact-list {
    position: absolute; left: 404px; top: 178px;
    list-style: none;
  }
  .contact-list li {
    display: flex; align-items: center; gap: 9px;
    font-size: 15px; color: var(--ink); height: 26px;
    white-space: nowrap;
  }
  .contact-list svg { width: 18px; height: 18px; flex: none; }

  .social-row {
    position: absolute; left: 408px; top: 272px;
    display: flex; gap: 12px;
  }
  .social-row span {
    width: 22px; height: 22px; border-radius: 6px;
    background: var(--icon-grey);
  }

  .back-field {
    position: absolute; left: 0; top: 0; right: 0; bottom: 34px;
    background: linear-gradient(180deg, #ffffff 0%, #f7f8f8 100%);
  }
</style>
</head>
<body>

<section class="card card--front" aria-label="Business card front">
  <p class="company-name">Brightwave Renewables</p>

  <div class="identity">
    <p class="identity__name">Daniel Mercer</p>
    <p class="identity__role">Director</p>
    <p class="identity__company">Brightwave Renewables LLC</p>
    <p class="identity__address">212 Harbor Street, Portland, ME 04101</p>
  </div>

  <div class="divider"></div>

  <ul class="contact-list">
    <li>
      <svg viewBox="0 0 18 18" aria-hidden="true"><circle cx="9" cy="9" r="9" fill="var(--brand-green)"/><rect x="4.5" y="6" width="9" height="6.5" fill="none" stroke="#fff" stroke-width="1.2"/><path d="M4.5 6 L9 9.5 L13.5 6" fill="none" stroke="#fff" stroke-width="1.2"/></svg>
      daniel.mercer@brightwave-renewables.com
    </li>
    <li>
      <svg viewBox="0 0 18 18" aria-hidden="true"><circle cx="9" cy="9" r="9" fill="var(--brand-green)"/><rect x="6" y="4" width="6" height="10" rx="1.2" fill="none" stroke="#fff" stroke-width="1.2"/><circle cx="9" cy="12" r="0.8" fill="#fff"/></svg>
      +1 (555) 014-2738
    </li>
    <li>
      <svg viewBox="0 0 18 18" aria-hidden="true"><circle cx="9" cy="9" r="9" fill="var(--brand-green)"/><rect x="5" y="7" width="8" height="5" fill="none" stroke="#fff" stroke-width="1.2"/><rect x="6.5" y="4.5" width="5" height="2.5" fill="#fff"/><rect x="6.5" y="10.5" width="5" height="3" fill="#fff"/></svg>
      555-019-4461
    </li>
  </ul>

  <div class="social-row" aria-label="Social profiles">
    <span></span><span></span><span></span><span></span>
  </div>

  <div class="footer-band"></div>
  <div class="footer-tab">daniel.mercer@brightwave-renewables.com</div>
</section>

<section class="card card--back" aria-label="Business card back">
  <div class="back-field" role="img" aria-label="Faint repeating brand pattern across the card back"></div>
  <p class="company-name">Brightwave Renewables</p>
  <div class="footer-band"></div>
  <div class="footer-tab">daniel.mercer@brightwave-renewables.com</div>
</section>

</body>
</html>
```